Principle Minded Business and Life skills coach needs inspiring Wordpress design

I need a wordpress design for a new company I am starting called Rise4Bloom. I help ordinary people and entrepreneurs develop the skills, techniques and focus needed to succeed and lead a rewarding life. This site's objective is to promote my ability to help the visitor, give him quality info he can use now, and display subtle ads and offers that the visitor can purchase to help him implement what I am teaching him.

I am a devoted husband and loving father. I've owned several companies primarily in the technology and energy fields. I need a site that helps my clients feel connected with me and allows them to believe that I WILL help them achieve their goals.

I will be writing articles and blogs on this site as well as promoting products (third party products and ads to start, and my own later on).
Updates

Additional websites in market:http://www.pathguidehub.com/ Added Wednesday, January 21, 2015

Target Market(s)

starting entrepreneurs, struggling business people, people looking for personal growth, people looking for a home base business, network marketers.

Industry/Entity Type

Business

Requirements
Must have
• Blog
• Areas for adsense and other advertising
Nice to have
• My picture in the header
• Ability for my customers to book an appointment with me.
• Websites in similar market:
• http://brightstridecoach.com/
• http://tomvarkendalejournal.com/
• http://moneycompassguide.com/
• http://brennickgrowthtraining.com/

```html
<!DOCTYPE html>
<html lang="en">
<head>
<meta charset="utf-8">
<title>Rise4Bloom – Life Coaching</title>
<link href="https://fonts.googleapis.com/css2?family=Source+Sans+3:ital,wght@0,400;0,600;0,700;1,400&display=swap" rel="stylesheet">
<style>
:root{
  --brand-dark:#1a4f7a;
  --brand-mid:#2a6f9e;
  --nav-top:#4aa6e2;
  --nav-bottom:#3690d2;
  --nav-active:#2f7fbf;
  --hero-box:#3e9ddb;
  --text-muted:#8899a6;
  --card-border:#d9dee2;
  --cta-band:#1f6892;
  --cta-edge:#4a92bd;
  --footer:#0e4468;
  --btn-cta-top:#40b3ea;
  --btn-cta-bottom:#1e8fd0;
  --page:#fbfcfc;
}
*{margin:0;padding:0;box-sizing:border-box}
html,body{width:1024px;height:1200px;overflow:hidden}
body{position:relative;background:var(--page);font-family:"Source Sans 3",sans-serif;color:var(--text-muted)}
.abs{position:absolute}

/* header */
.site-header{left:0;top:0;width:1024px;height:56px;background:#fff}
.logo{left:136px;top:13px;font-size:27px;font-weight:700;color:var(--brand-dark);letter-spacing:-.3px}
.contact-item{top:21px;font-size:9px;color:#2f86c8;display:flex;align-items:center;gap:5px}
.contact-mail{left:672px}
.contact-phone{left:804px}

/* nav */
.main-nav{left:0;top:56px;width:1024px;height:40px;background:linear-gradient(var(--nav-top),var(--nav-bottom));border-top:1px solid #2a7fc0}
.nav-item{top:0;height:40px;line-height:40px;font-size:11px;font-weight:700;color:#fff}
.nav-home{left:134px;width:72px;text-align:center;background:var(--nav-active)}
.social-dot{width:22px;height:22px;border-radius:50%;background:#fff}

/* hero */
.hero-photo{left:0;top:96px;width:1024px;height:456px;background:linear-gradient(100deg,#3f5a3a 0%,#6f8a6a 18%,#6fb0de 30%,#8cc6ec 48%,#d9dcc2 62%,#efeed8 80%,#e6e7cf 100%)}
.hero-box{left:570px;top:217px;width:454px;height:197px;background:var(--hero-box);padding:28px 0 0 18px;color:#fff}
.hero-box h1{font-size:27px;line-height:35px;font-weight:700}
.hero-box p{margin-top:8px;font-size:14.5px;line-height:17.5px;width:300px;padding-left:3px}

/* cards */
.card{top:464px;width:240px;height:289px;background:#fff;border:1px solid var(--card-border)}
.card h2{position:absolute;left:17px;top:14px;font-size:19.5px;font-weight:400;color:var(--brand-dark)}
.card-image{position:absolute;left:11px;top:46px;width:216px;height:112px}
.card p{position:absolute;left:11px;top:171px;width:222px;font-size:10px;line-height:16px}
.btn-ghost{height:30px;border:1px solid #c7cdd1;border-radius:15px;background:linear-gradient(#fff,#eef0f1);font-size:10px;color:#9aa4ab;display:flex;align-items:center;justify-content:center;gap:5px}
.card .btn-ghost{position:absolute;left:12px;top:234px;width:87px}
.field{position:absolute;left:21px;width:202px;height:29px;border:1px solid #dfe3e6;font-size:9px;color:#6d7880;padding:10px 0 0 10px}
.note{position:absolute;left:24px;top:202px;font-size:8.5px}

/* about & testimonial */
.section-title{top:778px;font-size:19.5px;color:var(--brand-dark)}
.dotted{top:814px;height:4px;border-top:1px dotted #b9c1c6;border-bottom:1px dotted #b9c1c6}
.coach-photo{left:139px;top:828px;width:239px;height:167px;background:linear-gradient(120deg,#2f3a2a,#6e6050 40%,#b08a72 70%,#4c8ac2)}
.coach-text{left:395px;top:842px;width:220px;font-size:10px;line-height:14.5px}
.coach-text p+p{margin-top:14px}
.avatar{left:725px;top:830px;width:70px;height:70px;border-radius:50%;background:radial-gradient(circle at 50% 55%,#c9a088,#5a3d2e 75%)}
.client-name{left:647px;top:911px;width:226px;text-align:center;font-size:12px}
.client-place{left:647px;top:928px;width:226px;text-align:center;font-size:9.5px;color:#7a858d}
.quote{left:658px;top:949px;width:210px;font-size:10px;line-height:16px;font-style:italic}

/* cta */
.cta-band{left:0;top:1050px;width:1024px;height:78px;background:var(--cta-band);border-top:4px solid var(--cta-edge)}
.cta-title{left:136px;top:1069px;font-size:19px;font-weight:700;color:#fff}
.cta-sub{left:136px;top:1094px;font-size:12.5px;color:#fff}
.cta-btn{left:694px;top:1070px;width:200px;height:42px;border-radius:5px;background:linear-gradient(var(--btn-cta-top),var(--btn-cta-bottom));border:1px solid #7fcdf2;color:#fff;font-size:14px;font-weight:700;display:flex;align-items:center;justify-content:center}

/* footer */
.site-footer{left:0;top:1128px;width:1024px;height:72px;background:var(--footer)}
.footer-links{left:144px;top:1147px;font-size:8.5px;font-weight:700;color:#fff;letter-spacing:.3px}
.copyright{left:143px;top:1173px;font-size:8.5px;color:#fff}
.foot-dot{width:21px;height:21px;border-radius:50%;background:#fff}
.foot-contact{left:715px;font-size:9px;font-weight:700;color:#fff;display:flex;align-items:center;gap:10px}
</style>
</head>
<body>

<header class="abs site-header">
</header>
<div class="abs logo">Rise4Bloom</div>
<div class="abs contact-item contact-mail">
  <svg width="24" height="12" viewBox="0 0 24 12"><path d="M0 3h5M2 6h4M0 9h5" stroke="#5aa3d8" stroke-width="1"/><rect x="8" y="1" width="15" height="10" fill="none" stroke="#5aa3d8"/><path d="M8 1l7.5 6L23 1" fill="none" stroke="#5aa3d8"/></svg>
  hello@rise4bloom.net
</div>
<div class="abs contact-item contact-phone">
  <svg width="14" height="14" viewBox="0 0 14 14"><path d="M3 1l2 3-1.5 1.5c.8 2 2.2 3.4 4 4L9 8l3 2-1.5 3C6 13 1 8 1 3z" fill="#5aa3d8"/><path d="M9 2a4 4 0 013 3M9 4a2 2 0 011 1" stroke="#5aa3d8" fill="none"/></svg>
  +61 555 010 247
</div>

<nav class="abs main-nav">
  <a class="abs nav-item nav-home">Home</a>
  <a class="abs nav-item" style="left:219px">About</a>
  <a class="abs nav-item" style="left:285px">Blog</a>
  <a class="abs nav-item" style="left:342px">Contact</a>
  <span class="abs social-dot" style="left:761px;top:9px"></span>
  <span class="abs social-dot" style="left:795px;top:9px"></span>
  <span class="abs social-dot" style="left:828px;top:9px"></span>
  <span class="abs social-dot" style="left:861px;top:9px"></span>
</nav>

<div class="abs hero-photo" role="img" aria-label="Smiling coach in a blue shirt outdoors with soft green foliage behind"></div>
<section class="abs hero-box">
  <h1>Make your life be what<br>you want it to be!</h1>
  <p>Lorem ipsum dolor sit amet, consectetur adipisic-ing elit, sed do eiusmod tempor incididunt ut labore et dolore magna aliqua.</p>
</section>

<article class="abs card" style="left:136px">
  <h2>Learn Life Design Basics</h2>
  <div class="card-image" role="img" aria-label="Two women talking on a white sofa" style="background:linear-gradient(90deg,#e9e6e0,#f4f3f0 50%,#dcdfe2)"></div>
  <p>Lorem ipsum dolor sit amet, consectetur adipisic-ing elit, sed do eiusmod tempor incididunt ut labore et dolore magna aliqua.</p>
  <a class="btn-ghost">Read More <span>›</span></a>
</article>

<article class="abs card" style="left:393px">
  <h2>What to do to grow</h2>
  <div class="card-image" role="img" aria-label="Couple chatting outdoors among green trees" style="background:linear-gradient(90deg,#8aa64a,#b5c86a 50%,#6f8f38)"></div>
  <p>Lorem ipsum dolor sit amet, consectetur adipisic-ing elit, sed do eiusmod tempor incididunt ut labore et dolore magna aliqua.</p>
  <a class="btn-ghost">Read More <span>›</span></a>
</article>

<aside class="abs card" style="left:648px">
  <h2 style="left:23px">Sign up for Newsletter</h2>
  <p style="left:23px;top:52px;width:205px">Lorem ipsum dolor sit amet, consectetur adipisicing elit, sed do eiusmod tempor incidi-dunt ut labore et dolore magna aliqua.</p>
  <div class="field" style="top:112px">Your Name</div>
  <div class="field" style="top:156px">Your Email</div>
  <div class="note">*Your email will be held in strictest confidentiality.</div>
  <a class="btn-ghost" style="left:21px;width:87px">Submit Now</a>
</aside>

<h2 class="abs section-title" style="left:140px">Meet Your Life Coach</h2>
<div class="abs dotted" style="left:138px;width:480px"></div>
<div class="abs coach-photo" role="img" aria-label="Portrait of the life coach"></div>
<div class="abs coach-text">
  <p>Tempor incididunt ut labore et dolore magna aliqua. Ut enim ad minim veniam, quis nostrud exercitation. Lorem ipsum dolor sit amet, con-sectetur adipisicing elit, sed do eiusmod</p>
  <p>Lorem ipsum dolor sit amet, consectetur adipisic-ing elit, sed do eiusmod</p>
</div>
<a class="abs btn-ghost" style="left:395px;top:965px;width:87px">Read More <span>›</span></a>

<h2 class="abs section-title" style="left:649px">Client Testimonial</h2>
<div class="abs dotted" style="left:647px;width:239px"></div>
<div class="abs avatar" role="img" aria-label="Client portrait"></div>
<div class="abs client-name">Mara Lindell</div>
<div class="abs client-place">Lyon, France</div>
<blockquote class="abs quote">“Lorem ipsum dolor sit amet, consectetur adipi-sicing elit, sed do eiusmod tempor incididunt ut labore et dolore magna aliqua.”</blockquote>

<section class="abs cta-band"></section>
<div class="abs cta-title">Book a Private Coaching Session Now.</div>
<div class="abs cta-sub">If you are ready to do the work, I am ready to help you get to the change you want in your life.</div>
<a class="abs cta-btn">Request Coaching Session</a>

<footer class="abs site-footer"></footer>
<div class="abs footer-links">LINKS &nbsp;| &nbsp;LINKS &nbsp;| &nbsp;LINKS &nbsp;| &nbsp;LINKS</div>
<div class="abs copyright">Copyright © 2015. All rights reserved. &nbsp;Company Name. Privacy Policy &nbsp;| &nbsp;Sitemap</div>
<span class="abs foot-dot" style="left:592px;top:1144px"></span>
<span class="abs foot-dot" style="left:624px;top:1144px"></span>
<span class="abs foot-dot" style="left:655px;top:1144px"></span>
<div class="abs foot-contact" style="top:1146px">
  <svg width="16" height="11" viewBox="0 0 16 11"><rect width="16" height="11" fill="#4a8ec0"/><path d="M0 0l8 6 8-6" fill="none" stroke="#0e4468"/></svg>
  contact@rise4bloom.net
</div>
<div class="abs foot-contact" style="top:1169px">
  <svg width="16" height="14" viewBox="0 0 14 14"><path d="M3 1l2 3-1.5 1.5c.8 2 2.2 3.4 4 4L9 8l3 2-1.5 3C6 13 1 8 1 3z" fill="#4a8ec0"/></svg>
  555-01934-27816
</div>

</body>
</html>
```